ALL TEXT GRAPHICS TM May 2025 for Instagram

We are looking for a series of social media graphics for Instagram (new size: 4:5 (1080 x 1350 pixels) ratio that are ALL TEXT. We want the following quotes below on each graphic; one quote per graphic. AND, In very small letters at the bottom of each graphic, add @TovaMarshOnline
The look and feel of these graphics should be complimentary to the color palette attached below; but keep them simple. But the design is up to you; at the end of this document, I provided various samples of all text graphics that I like as examples.
Target Market(s)
women looking to lose weight
Look and feel

```html
<!DOCTYPE html>
<html lang="en">
<head>
<meta charset="utf-8">
<title>All Text Graphics – TM</title>
<link href="https://fonts.googleapis.com/css2?family=Archivo+Black&family=Cormorant+Garamond:wght@400;500&display=swap" rel="stylesheet">
<style>
  :root {
    --page: #ffffff;
    --magenta: #f0087f;
    --hot-pink: #ff1a8c;
    --violet: #b0139a;
    --orange: #ffb347;
    --band-violet: #a012a0;
    --band-pink: #ff2a8a;
    --ink: #ffffff;
    --frame: rgba(255,255,255,0.9);
  }
  * { margin: 0; padding: 0; box-sizing: border-box; }
  html, body { width: 849px; height: 1200px; overflow: hidden; background: var(--page); }
  .sheet { position: relative; width: 849px; height: 1200px; }
  .post {
    position: absolute;
    width: 221px; height: 276px;
    background:
      linear-gradient(135deg, var(--orange) 0%, rgba(255,140,60,0.6) 8%, rgba(255,30,140,0) 22%),
      radial-gradient(circle at 70% 60%, var(--hot-pink) 0%, var(--magenta) 45%, var(--violet) 100%);
    overflow: hidden;
    color: var(--ink);
  }
  .post .frame { position: absolute; left: 12px; top: 12px; width: 197px; height: 223px; }
  .post .message {
    position: absolute; left: 10px; right: 10px; top: 10px; height: 227px;
    display: flex; flex-direction: column; justify-content: center; align-items: center;
    text-align: center; text-transform: uppercase;
  }
  .bold { font-family: "Archivo Black", sans-serif; font-size: 17px; line-height: 20.5px; letter-spacing: 0.2px; }
  .thin { font-family: "Cormorant Garamond", serif; font-weight: 500; font-size: 16.5px; line-height: 19px; letter-spacing: 0.3px; }
  .post .band {
    position: absolute; left: 0; right: 0; bottom: 0; height: 29px;
    background: linear-gradient(90deg, var(--band-violet), var(--band-pink));
    display: flex; align-items: center; justify-content: center;
  }
  .handle {
    font-family: "Archivo Black", sans-serif; font-size: 6px; letter-spacing: 0.2px;
    border: 1px solid var(--ink); border-radius: 8px; padding: 2px 8px; text-transform: uppercase;
  }
  .c1 { left: 84px; } .c2 { left: 314px; } .c3 { left: 545px; }
  .r1 { top: 34px; } .r2 { top: 319px; } .r3 { top: 605px; } .r4 { top: 890px; }
</style>
</head>
<body>
<svg width="0" height="0" style="position:absolute">
  <defs>
    <g id="corner-frame" fill="none" stroke="#ffffff" stroke-width="1.2">
      <path d="M0 12 Q0 0 12 0"/>
      <path d="M185 0 Q197 0 197 12"/>
      <path d="M0 211 Q0 223 12 223"/>
      <path d="M185 223 Q197 223 197 211"/>
    </g>
  </defs>
</svg>
<main class="sheet">

  <article class="post c1 r1">
    <svg class="frame" viewBox="0 0 197 223"><use href="#corner-frame"/></svg>
    <div class="message">
      <p class="bold">That<br>stubborn<br>weight?</p>
      <p class="thin">It's not your fault.<br>Your hormones<br>are to blame<br>and you're<br>not alone;</p>
      <p class="bold">But there<br>is a fix.</p>
    </div>
    <div class="band"><span class="handle">@TovaMarshOnline</span></div>
  </article>

  <article class="post c2 r1">
    <svg class="frame" viewBox="0 0 197 223"><use href="#corner-frame"/></svg>
    <div class="message">
      <p class="bold">Tired.<br>Moody.</p>
      <p class="thin">Stubborn<br>belly fat.<br>Your hormones<br>are screaming<br>for help!</p>
      <p class="bold">Let's fix<br>that.</p>
    </div>
    <div class="band"><span class="handle">@TovaMarshOnline</span></div>
  </article>

  <article class="post c3 r1">
    <svg class="frame" viewBox="0 0 197 223"><use href="#corner-frame"/></svg>
    <div class="message">
      <p class="bold">Your belly<br>isn't fat...</p>
      <p class="thin">It's hormonal.<br>And here's<br>how to fix it.</p>
      <p class="bold">Comment<br>hormones</p>
      <p class="thin">if nothing<br>is working.</p>
    </div>
    <div class="band"><span class="handle">@TovaMarshOnline</span></div>
  </article>

  <article class="post c1 r2">
    <svg class="frame" viewBox="0 0 197 223"><use href="#corner-frame"/></svg>
    <div class="message">
      <p class="bold">The<br>stubborn<br>belly fat<br>after 40?</p>
      <p class="thin">It's not about<br>calories;<br>it's about<br>your hormones.</p>
      <p class="bold">Here is<br>the fix!</p>
    </div>
    <div class="band"><span class="handle">@TovaMarshOnline</span></div>
  </article>

  <article class="post c2 r2">
    <svg class="frame" viewBox="0 0 197 223"><use href="#corner-frame"/></svg>
    <div class="message">
      <p class="thin">Flat tummy<br>in your 40<span style="text-transform:none">s</span>?<br>It's still possible!</p>
      <p class="bold">Comment<br>bye belly<br>to get the<br>10 secrets</p>
      <p class="thin">to a flatter<br>tummy</p>
    </div>
    <div class="band"><span class="handle">@TovaMarshOnline</span></div>
  </article>

  <article class="post c3 r2">
    <svg class="frame" viewBox="0 0 197 223"><use href="#corner-frame"/></svg>
    <div class="message">
      <p class="bold">Bloating.<br>Muffin top.<br>Puffy<br>waistline.</p>
      <p class="thin">Your body's<br>screaming<br>for a different<br>kind of fix.</p>
      <p class="bold">Here it is</p>
    </div>
    <div class="band"><span class="handle">@TovaMarshOnline</span></div>
  </article>

  <article class="post c1 r3">
    <svg class="frame" viewBox="0 0 197 223"><use href="#corner-frame"/></svg>
    <div class="message">
      <p class="thin">You're doing<br>all the “right”<br>things,<br>but your belly<br>won't go down?</p>
      <p class="bold">Here's what<br>you haven't<br>tried.</p>
    </div>
    <div class="band"><span class="handle">@TovaMarshOnline</span></div>
  </article>

  <article class="post c2 r3">
    <svg class="frame" viewBox="0 0 197 223"><use href="#corner-frame"/></svg>
    <div class="message">
      <p class="bold">This 90-day<br>plan</p>
      <p class="thin">helped women<br>over 40 slim down,<br>get a tiny<br>waist and feel<br>sexy again.</p>
      <p class="bold">You're next.</p>
    </div>
    <div class="band"><span class="handle">@TovaMarshOnline</span></div>
  </article>

  <article class="post c3 r3">
    <svg class="frame" viewBox="0 0 197 223"><use href="#corner-frame"/></svg>
    <div class="message">
      <p class="thin">This is the secret<br>women over 40<br>are using<br>to get snatched;<br>without starving.</p>
      <p class="bold">Comment<br>skinny<br>to get<br>the exact<br>plan.</p>
    </div>
    <div class="band"><span class="handle">@TovaMarshOnline</span></div>
  </article>

  <article class="post c1 r4">
    <svg class="frame" viewBox="0 0 197 223"><use href="#corner-frame"/></svg>
    <div class="message">
      <p class="thin">What worked<br>in your 30<span style="text-transform:none">s</span><br>won't work now.</p>
      <p class="bold">Here's what<br>actually<br>does.</p>
      <p class="thin">Drop 30 pounds<br>in 3 months.</p>
    </div>
    <div class="band"><span class="handle">@TovaMarshOnline</span></div>
  </article>

</main>
</body>
</html>
```